Kaffeerösterei sucht Etiketten-Design
- schnelle Ausführung - mein Geschmack voll getroffen - unkompliziert und Kunden orientiert bei der Ausführung
Zielgruppe
Kaffeerösterei für die edelsten und teuersten Rohkaffees.
Meine Kunden sind Kaffee Geniesser.
Aufgabenstellung
Transparente Aufkleber für eine Schiefertafel im Format 22.5 cm x 15.5 cm.
Im Hand-Lettering Stil.
5 Schiefertafeln sind gewünscht.
Tafel 1
Kostenlos zur Degustation
Espresso
Café Crème 3.--
Americano 3.--
Filter Kaffee 3.--
Tafel 2
Kaffee & Milch
Cappuccino 4.--
Café Latte 4.--
Flat White 4.--
Latte Macchiato 4.--
Latte Macchiato mit Aroma 5.--
Kaffee & Hafermilch + 1.--
Tafel 3
Crepes
Pikant
- Pizza Crepes 7.--
- Flammkuchen Crepes 7.--
Süss
- Schoggi Crepes 6.--
- Apfelmus & Zimtzucker 6.--
Tafel 4
Kaffee & Schnaps
- Original Entlebucher Schwarzes 7.--
- Espresso Coretto 5.00
- Schwarzes mit Rahmhaube 8.--
Tafel 5
Schokolade & Milch
- heisse Schoggi 5.--
- heisse Schoggi mit Rahmhaube 6.--
- heisse Schoggi mit Espresso 6.--
- Schokolade & Hafermilch +1.--
Als Idee, was mir gefallen könnte:
https://www.bildsammlung.example/pin/104857392018374655/
https://de.grafikhort.example/vektorkunst/4418203-set-kaffeekarte-mit-tassen-kaffeegetranken-im-vintage-stil-stilisierte-zeichnung-mit-kreide-auf-tafel-schriftzug-sample-drinks
https://www.fotolager.example/stockfoto-heisser-kakao-bar-warm-hier-oben-hand-tafel-caf-schild-an-tafel-hintergrund-mit-farbe-kreide-schriftzug-werbung-fur-heisse-d-583021746.html

```html
<!DOCTYPE html>
<html lang="de">
<head>
<meta charset="utf-8">
<title>Crepes – Schiefertafel</title>
<link rel="stylesheet" href="https://fonts.googleapis.com/css2?family=Amatic+SC:wght@700&family=Kaushan+Script&display=swap">
<style>
  :root {
    --paper: #ffffff;
    --slate: #1d1d1b;
    --title-cream: #fff9da;
    --accent-pink: #efb0b1;
    --price-cream: #fdebd2;
    --chalk-white: #ffffff;
  }
  html, body {
    margin: 0;
    padding: 0;
    width: 1200px;
    height: 869px;
    overflow: hidden;
    background: var(--paper);
  }
  .menu-board {
    display: block;
    width: 1200px;
    height: 869px;
  }
  .board-surface { fill: var(--slate); }
  .board-title {
    font-family: "Kaushan Script", cursive;
    font-size: 112px;
    fill: var(--title-cream);
  }
  .section-heading {
    font-family: "Kaushan Script", cursive;
    font-size: 64px;
    fill: var(--accent-pink);
  }
  .dish-name {
    font-family: "Amatic SC", sans-serif;
    font-weight: 700;
    font-size: 74px;
    letter-spacing: 3px;
    fill: var(--chalk-white);
  }
  .dish-price {
    font-family: "Kaushan Script", cursive;
    font-size: 62px;
    fill: var(--price-cream);
  }
  .ornament-area { fill: var(--title-cream); opacity: 0.22; }
  .cutlery-area { fill: var(--chalk-white); opacity: 0.14; }
</style>
</head>
<body>
<svg class="menu-board" viewBox="0 0 1200 869" xmlns="http://www.w3.org/2000/svg">
  <rect class="board-surface" x="65" y="69" width="1065" height="734"/>

  <rect class="ornament-area" x="339" y="160" width="78" height="42" rx="14" role="img" aria-label="Verschnörkeltes Zierelement links vom Titel"/>
  <rect class="ornament-area" x="778" y="160" width="78" height="42" rx="14" role="img" aria-label="Verschnörkeltes Zierelement rechts vom Titel"/>

  <text class="board-title" x="596" y="207" text-anchor="middle">Crepes</text>

  <rect class="cutlery-area" x="140" y="259" width="116" height="256" rx="18" role="img" aria-label="Gezeichnetes Besteck: Messer und Gabel in weißer Kreidelinie"/>

  <text class="section-heading" x="596" y="312" text-anchor="middle">Pikant</text>

  <g class="dish-list">
    <text class="dish-name" x="824" y="393" text-anchor="end">Pizza Crepes</text>
    <text class="dish-price" x="869" y="393">7,–</text>

    <text class="dish-name" x="824" y="472" text-anchor="end">Flammkuchen Crepes</text>
    <text class="dish-price" x="869" y="472">7,–</text>
  </g>

  <text class="section-heading" x="596" y="568" text-anchor="middle">Süss</text>

  <g class="dish-list">
    <text class="dish-name" x="824" y="647" text-anchor="end">Schoggi Crepes</text>
    <text class="dish-price" x="869" y="647">6,–</text>

    <text class="dish-name" x="824" y="731" text-anchor="end">Apfelmus &amp; Zimtzucker</text>
    <text class="dish-price" x="869" y="731">6,–</text>
  </g>
</svg>
</body>
</html>
```